CBD Boutique Business Card Needed

We are in need of a business card to reflect the direction of our latest products. We are a fully organic company in which our store and products are very heavy in wood and "natural" components. We decided to bring color into one of our brands and immediately knew this is where we needed to go.

We are NOT a cash grab CBD company. We could have done this wrong, slapped a label on a shit product and left it like that. I am passionate about sharing my experience with other veterans and opening a store and making it a comfortable place for others to come and see if they can have the same experience.

Target Market(s)

We are a dual market company. We do have a beauty line that will cover the costs of the majority of our business. But we also heavily cater to veterans and first responders. I am a veteran and this is how I found out about CBD. So the marketing needs to bring in our higher end beauty clientele but also be able to not put off our customers that readily need this.

Contact Information for Business Card

What we are looking for is a light, professional, boutique design that is is neither quite feminine or masculine. Attached is a picture of a store in Portland that we asked our store designer to get her inspiration from. But all natural wood and black outlines are what is mostly in there.

Attached are the following files:

Logo: An AI file with how we have our logo. I do not understand AI and have no idea why the letters are individual. The font is Adam. OLU is the logo and Tonics of Vigor is our tagline.

KM Vantage (front and back) cards I did originally found at a trade show that I absolutely loved...while it is mostly there and I would still be happy with them but it is me pretending to be you. I understand I am not and there is probably a lot wrong that all of you would see instantly and this is why I am here.

Dropper Bottle: This is our final product mock up

Water Color: I am semi flexible here. This water color is slightly different on every level of our brand. The color itself can change...we are not stuck on THIS particular one. If you happen to make a new one that is similar in style and we use it...then I will happily commission you to change the rest on our next product run. I am pretty sure you can use this statement as evidence later . =) .

But seriously, we heavily believe in pay it forward and will work with anyone here that may have a vision bigger than ours. The winner of this contest will get preferential consideration on our marketing materials (need letterhead etc. next, as well as a brochure, and website) so three more projects coming down the pipeline.

Information to use for your mockup is contained on the card images I have included. I would prefer CBD for wellness CBD for life to be more prominent. No where else on the card do we have CBD mentioned.

Font styles to use
Sans Serif

Colors

Designer to choose colors to be used in the design.

Requirements
Must have
• Double Sided
• Front: OLU logo on front of card will be raised embossed. Background is watercolor. One has been provided. Others are up for consideration. If the rest of your design is incredible and I don't like your watercolor I will just ask to swap it.
• Back: Standard information. Not stuck on anything here. I LOVE clean minimal designs. The bleed on the card I provided is a luxury...
• Font for title and OLU is Adam. Everything else I prefer san serif or as clean as possible.
Nice to have
• I Need to incorporate Naturally Nurturing somewhere on the card. Bold but not intrusive.

```html
<!DOCTYPE html>
<html lang="en">
<head>
<meta charset="utf-8">
<title>OLU – Tonics of Vigor Business Card</title>
<link rel="stylesheet" href="https://fonts.googleapis.com/css2?family=Open+Sans:wght@300;400;700&display=swap">
<style>
  :root {
    --backdrop: #e4e4e4;
    --mint: #bfe6cf;
    --leaf: #8fd07f;
    --moss: #74c67a;
    --lime: #c9e36a;
    --ink: #111111;
    --paper: #ffffff;
    --card-w: 540px;
    --card-h: 308px;
  }
  * { box-sizing: border-box; margin: 0; padding: 0; }
  html, body {
    width: 1200px;
    height: 800px;
    overflow: hidden;
    background: var(--backdrop);
    font-family: "Open Sans", Arial, sans-serif;
  }
  .canvas {
    width: 1200px;
    height: 800px;
    display: flex;
    align-items: center;
    justify-content: center;
    gap: 40px;
  }
  .card {
    position: relative;
    width: var(--card-w);
    height: var(--card-h);
    overflow: hidden;
    box-shadow: 0 6px 18px rgba(0,0,0,0.14);
  }
  .watercolor {
    position: absolute;
    inset: 0;
    background:
      radial-gradient(ellipse 40% 55% at 20% 25%, rgba(116,198,122,0.55), transparent 70%),
      radial-gradient(ellipse 35% 45% at 78% 30%, rgba(201,227,106,0.8), transparent 70%),
      radial-gradient(ellipse 45% 40% at 35% 80%, rgba(191,230,207,0.9), transparent 70%),
      radial-gradient(ellipse 40% 50% at 85% 85%, rgba(143,208,127,0.7), transparent 70%),
      linear-gradient(120deg, var(--mint) 0%, var(--leaf) 45%, var(--lime) 100%);
  }
  .wordmark {
    position: absolute;
    display: flex;
    flex-direction: column;
    align-items: center;
    font-weight: 300;
  }
  .wordmark-name {
    font-size: 64px;
    letter-spacing: 6px;
    line-height: 1;
  }
  .wordmark-tagline {
    font-size: 14px;
    letter-spacing: 2px;
    text-transform: uppercase;
    margin-top: 6px;
  }
  .card-front .wordmark {
    color: var(--paper);
    left: 50%;
    top: 50%;
    transform: translate(-50%, -55%);
  }
  .card-back .wordmark {
    color: var(--ink);
    left: 140px;
    top: 150px;
    transform: translate(-50%, -50%);
  }
  .card-back .wordmark-name { font-size: 50px; letter-spacing: 5px; }
  .card-back .wordmark-tagline { font-size: 11px; letter-spacing: 1.5px; }
  .divider {
    position: absolute;
    left: 268px;
    top: 92px;
    width: 1px;
    height: 104px;
    background: var(--ink);
  }
  .contact {
    position: absolute;
    left: 284px;
    top: 92px;
    color: var(--ink);
  }
  .contact-name {
    font-size: 15px;
    font-weight: 700;
    letter-spacing: 0.5px;
  }
  .contact-title {
    font-size: 12px;
    margin-bottom: 8px;
  }
  .contact-list { list-style: none; }
  .contact-list li {
    display: flex;
    align-items: center;
    gap: 7px;
    font-size: 11px;
    line-height: 17px;
  }
  .contact-list svg { width: 10px; height: 10px; flex: none; }
  .address-band {
    position: absolute;
    left: 0;
    right: 0;
    top: 256px;
    height: 22px;
    background: var(--ink);
    color: var(--paper);
    font-size: 11px;
    text-align: right;
    padding-right: 20px;
    line-height: 22px;
  }
</style>
</head>
<body>
<main class="canvas">
  <section class="card card-front" aria-label="Card front">
    <div class="watercolor" role="img" aria-label="Green and lime watercolor wash background"></div>
    <div class="wordmark">
      <span class="wordmark-name">OLU</span>
      <span class="wordmark-tagline">Tonics of Vigor</span>
    </div>
  </section>

  <section class="card card-back" aria-label="Card back">
    <div class="watercolor" role="img" aria-label="Green and lime watercolor wash background"></div>
    <div class="wordmark">
      <span class="wordmark-name">OLU</span>
      <span class="wordmark-tagline">Tonics of Vigor</span>
    </div>
    <div class="divider"></div>
    <div class="contact">
      <p class="contact-name">YOUR NAME</p>
      <p class="contact-title">Your Title</p>
      <ul class="contact-list">
        <li>
          <svg viewBox="0 0 10 10" aria-hidden="true"><path d="M2 0.8 L3.6 0.8 L4.2 3 L3 3.8 Q4 6 6.2 7 L7 5.8 L9.2 6.4 L9.2 8 Q9 9.4 7.6 9.2 Q1 8.2 0.8 2.2 Q0.8 0.8 2 0.8 Z" fill="currentColor"/></svg>
          123-456-2100
        </li>
        <li>
          <svg viewBox="0 0 10 10" aria-hidden="true"><rect x="0.5" y="2" width="9" height="6.5" fill="currentColor"/><path d="M0.8 2.3 L5 5.6 L9.2 2.3" fill="none" stroke="#bfe6cf" stroke-width="0.9"/></svg>
          youremail@mailbox.com
        </li>
        <li>
          <svg viewBox="0 0 10 10" aria-hidden="true"><circle cx="5" cy="5" r="4.4" fill="none" stroke="currentColor" stroke-width="1"/><ellipse cx="5" cy="5" rx="1.8" ry="4.4" fill="none" stroke="currentColor" stroke-width="0.8"/><line x1="0.6" y1="5" x2="9.4" y2="5" stroke="currentColor" stroke-width="0.8"/></svg>
          www.yourwebsite.com
        </li>
      </ul>
    </div>
    <div class="address-band">Your address, city, state, ZIP 0000</div>
  </section>
</main>
</body>
</html>
```